Business Card Design Project

I am a Chiropractor that is looking for a new business card.  Our logo was slightly changed lately, therefore need a new, more professional look.
We are a modern, non-stuffy chiropractic office.  Want a contemporary look that will let people know this is not your typical doctors office.  Our logo is red, and contains the name of our business: realign.  The u in the logo is green, stressing the most important part of our business: "u"

Target Market(s)
moderate to upper income bracket, family friendly
www.realignspine-example.com
Gordon Pell
Family Chiropractor
314 Hollis Rd
Fernhollow, ST 00999
555.555.0147 phone
555.555.0148 fax
Industry/Entity Type
Business
Requirements
Must have
- www.realignspine-example.com
Gordon Pell
Family Chiropractor
314 Hollis Rd
Fernhollow, ST 00999
555.555.0147 phone
555.555.0148 fax

```html
<!DOCTYPE html>
<html lang="en">
<head>
<meta charset="utf-8">
<title>Realign — Business Card</title>
<link href="https://fonts.googleapis.com/css2?family=Arimo:wght@400;700&display=swap" rel="stylesheet">
<style>
  :root {
    --red: #e8473f;
    --green: #5aa832;
    --grey: #9a9a9a;
    --white: #ffffff;
    --backdrop: #e9e7e4;
  }
  * { margin: 0; padding: 0; box-sizing: border-box; }
  html, body {
    width: 1200px; height: 981px; overflow: hidden;
    background: var(--backdrop);
    font-family: "Arimo", Arial, sans-serif;
  }
  .sheet {
    width: 1200px; height: 981px;
    display: flex; flex-direction: column;
    align-items: center; justify-content: center; gap: 60px;
  }
  .card {
    position: relative;
    width: 660px; height: 377px;
    background: var(--white);
    overflow: hidden;
    box-shadow: 0 6px 18px rgba(0,0,0,0.18);
  }
  /* Front */
  .front .top-band {
    position: absolute; left: 300px; top: 0;
    width: 360px; height: 20px; background: var(--red);
  }
  .front .top-block {
    position: absolute; left: 300px; top: 20px;
    width: 150px; height: 34px; background: var(--red);
  }
  .front .corner-block {
    position: absolute; right: 0; bottom: 0;
    width: 70px; height: 60px; background: var(--red);
  }
  .identity {
    position: absolute; left: 70px; top: 200px;
  }
  .identity .name {
    color: var(--green); font-weight: 700; font-size: 29px; line-height: 1;
  }
  .identity .title {
    color: var(--grey); font-size: 13px; margin-top: 4px;
  }
  .contact {
    position: absolute; left: 425px; top: 180px;
    font-size: 13px; line-height: 19px;
  }
  .contact .line { display: flex; align-items: center; gap: 8px; color: var(--red); white-space: nowrap; }
  .contact .tag {
    display: inline-flex; align-items: center; justify-content: center;
    width: 12px; height: 12px; border-radius: 2px;
    background: var(--green); color: var(--white);
    font-size: 9px; font-weight: 700;
  }
  .contact .address { color: var(--green); margin-top: 6px; }
  /* Back */
  .back .band {
    position: absolute; left: 0; width: 100%; height: 92px; background: var(--red);
  }
  .back .band.upper { top: 0; }
  .back .band.lower { bottom: 0; }
  .brand {
    position: absolute; left: 0; top: 92px; width: 100%; height: 193px;
    display: flex; align-items: center; justify-content: center; gap: 18px;
  }
  .brand .dot {
    width: 22px; height: 22px; border-radius: 50%; background: var(--green);
  }
  .brand .wordmark {
    color: var(--red); font-size: 68px; font-weight: 400; letter-spacing: 2px;
  }
</style>
</head>
<body>
<main class="sheet">
  <section class="card front" aria-label="Business card front">
    <div class="top-band"></div>
    <div class="top-block"></div>
    <div class="corner-block"></div>
    <div class="identity">
      <div class="name">Gordon Pell</div>
      <div class="title">Family Chiropractor</div>
    </div>
    <div class="contact">
      <div class="line"><span class="tag">p</span>555.555.0147</div>
      <div class="line"><span class="tag">f</span>555.555.0148</div>
      <div class="line"><span class="tag">w</span>www.realignspine-example.com</div>
      <div class="address">314 Hollis Rd<br>Fernhollow, ST 00999</div>
    </div>
  </section>

  <section class="card back" aria-label="Business card back">
    <div class="band upper"></div>
    <div class="brand">
      <span class="dot"></span>
      <span class="wordmark">realign</span>
    </div>
    <div class="band lower"></div>
  </section>
</main>
</body>
</html>
```